Bottle labels and logo for small distillery

Harbor Stillhouse is a small beginning project of handcrafted distillery producing cider spirit (same as apple wine spirit) and apple vodka from apple wine. There are not many similar small distilleries in the Baltic Sea region and very few of them produce apple brandy, so the concept and the product itself are unique. That is the reason we are not developing any distinctive brand and we are sticking to two elements – company name ‘Harbor Stillhouse OÜ’ and product name ‘Orchardine’. Best branding solution for us would be to have a clear logo instead of words.

In the future it is most likely that the product range will broaden by some type of sweet liqueurs like apple-liqueur and black-currant-liqueur and both will be mixtures of natural juice and apple brandy.

We have tested the product itself and more or less chosen proper bottle and closing. Example of the shape of the bottle:

https://www.vessel-depot.example.co.uk/Glass-vessels/Glass-vessels/500ml-glass-vessels/500ml-clear-glass-vessel-Rondel.html

Sizes of bottles:
500 ml Height (without cap) 350 mm, external diameter 60 mm;
375 ml Height (without cap) 330 mm, external diameeter 55 mm;

The bottle cap/closing is going to be waxed, and should look something like that:

http://img.picstash-example.com/qR7Tz.jpg

The design has two separate parts: (1) paper bottle label and (2) print on the bottle.

Front side – printed to the bottle, preferably a symbol without text, for better quality of print rather a vector graphics (monochrome or up to 3-single colour picture). We would like to use the symbol also as an enterprise logo if possible (but logo and bottle print can also be different if designer decides so). It should give a hint to apple based distillate (but, we do not want to narrow down creators fantasy so if you have a good idea please don’t hold back). Just to offer a dumb examples:
https://moodbinder-example.com/entry/51839206
https://www.pinboardly-example.ca/pin/719302846615902418/?lp=true https://www.stockframe-example.com/image-vector/decorative-apple-flora-ornaments-leaf-flower-482017356?src=QXP_tbRkLw8YpH3JcV_29m-2-50
NB! these are just examples of style, contents are more or less random.

Back side – a rectangular shaped label glued to the bottle. Label should not be a square but rather oblong and narrow. The colour of the label shouldn’t be white but rather light yellow, light brown or light creamy. Some examples:

https://www.pinboardly-example.co.uk/pin/830174529266108354 https://www.pinboardly-example.co.uk/pin/591840372605183924

Label has to contain such information:
1) (Product in large print) Orchardine
2) (product) apple wine spirit
3) (Neto amount) 50 cl; / 35 cl
4) (Ethanol in large print) 45%; / 55%
5) (Producer) Produced by Harbor Stillhouse, Lõunamaa 48213, Rannaküla, Sõstra 7;
6) (raw material and technology) Made in Estonia. Product is made of Estonian apple wine and distilled in reflux still in small batches
7) (distillate) Distillate 85%
8) (batch no) Batch no: (stamp) …
9) (note) produced with utmost pleasure
10) (note) Consume responsibly
11) (signature) distiller: …

We also need the label to be designed in Estonian as follows:
1) Orchardine
2) Õunaveini destillaat
3) 50 cl; / 35 cl
4) 45% / 55%
5) Toodetud Harbor Stillhouse OÜ poolt, Lõunamaal 48213, Rannaküla, Sõstra 7;
6) Toodetud Eestis, eestimaisest õunaveinist ja destilleeritud käsitööna väikeste partiidena
7) Destillaat 85%
8) Partii nr:
9) Toodetud puhtast rõõmust
10) Tarbige vastutustundlikult!
11) Meister:

Design as such can be the same. Since we are planning to bottle the product in 375 ml and 500 ml bottles and dilute it down to 45% and 55%. So, there should be 37,5 cl 45%, 50 cl 45%; 37,5 cl 55%; 50 cl 55%.

We assume that in case of 37,5 cl and 50 cl bottles we can use the same design and just resize the printed image and paper-label a bit.

Since the product is handmade and high quality we would like to stress credibility. Not as important as the first purchase is the second purchase of clients – the label should not be shocking but rather trustworthy. And classy in the very best sense.

We are hoping to have a long term business relationship with possible future designer.

Target Market(s)

Adult male alcohol consumers

Industry/Entity Type

Food Production

Logo Text

Harbor Stillhouse

Colors

Designer to choose colors to be used in the design.

```html
<!DOCTYPE html>
<html lang="et">
<head>
<meta charset="utf-8">
<title>Orchardine – bottle labels</title>
<link rel="stylesheet" href="https://fonts.googleapis.com/css2?family=Arimo:wght@400;700&family=Roboto+Condensed:wght@700;800&family=Crimson+Pro:wght@700&display=swap">
<style>
  :root {
    --paper: #fffdd0;
    --halo: #fdfbc9;
    --frame: #9a6534;
    --wine: #960b0b;
    --ink: #2a2a2a;
    --art-light: #c8463c;
    --art-mid: #a5231c;
    --art-dark: #6e1410;
  }
  * { margin: 0; padding: 0; box-sizing: border-box; }
  html, body { width: 1200px; height: 1043px; overflow: hidden; background: #fff; }
  .canvas { position: relative; width: 1200px; height: 1043px; font-family: "Arimo", Arial, sans-serif; color: var(--ink); }

  .label { position: absolute; }
  .label-halo { position: absolute; inset: 0; background: var(--halo); border-radius: 160px; }
  .label-frame { position: absolute; background: var(--paper); border: 5px solid var(--frame); border-radius: 140px; }

  .art-area {
    position: absolute;
    border-radius: 50%;
    background: radial-gradient(circle at 40% 40%, var(--art-light) 0%, var(--art-mid) 55%, var(--art-dark) 100%);
  }

  .line { position: absolute; left: 0; width: 100%; text-align: center; white-space: nowrap; }
  .wordmark { font-family: "Roboto Condensed", sans-serif; font-weight: 800; color: var(--wine); }
  .product-big { font-family: "Roboto Condensed", sans-serif; font-weight: 800; color: var(--wine); }
  .product-title { font-family: "Roboto Condensed", sans-serif; font-weight: 800; color: var(--ink); }
  .bold { font-weight: 700; }
  .maker-serif { font-family: "Crimson Pro", serif; font-weight: 700; }
  .left-text { text-align: left; width: auto; }
</style>
</head>
<body>
<div class="canvas">

  <!-- Front label -->
  <section class="label label-front" style="left:23px; top:42px; width:369px; height:950px;">
    <div class="label-halo"></div>
    <div class="label-frame" style="left:9px; top:23px; width:356px; height:906px;"></div>
    <div class="art-area" role="img" aria-label="Red apple illustration with leaves and a white still-coil pattern" style="left:56px; top:58px; width:267px; height:329px;"></div>
    <div class="line wordmark" style="top:405px; font-size:54px; line-height:60px;">Orchardine</div>
    <div class="line product-big" style="top:513px; font-size:68px; line-height:75px;">Apple<br>Wine<br>Spirit</div>
    <div class="line" style="top:816px; font-size:23px; line-height:26px;">Produced by:</div>
    <div class="line maker-serif" style="top:849px; font-size:33px; line-height:38px;">Harbor Stillhouse</div>
  </section>

  <!-- English back label -->
  <section class="label label-back-en" style="left:417px; top:35px; width:373px; height:940px;">
    <div class="label-halo"></div>
    <div class="label-frame" style="left:8px; top:22px; width:358px; height:901px;"></div>
    <div class="art-area" role="img" aria-label="Small red apple illustration with leaves and a white still-coil pattern" style="left:126px; top:36px; width:121px; height:150px;"></div>
    <div class="line wordmark" style="top:199px; font-size:26px; line-height:28px;">Orchardine</div>
    <div class="line product-title" style="top:248px; font-size:28px; line-height:30px;">Apple Wine Spirit</div>
    <div class="line" style="top:293px; font-size:28px; line-height:30px;">50 cl/35 cl</div>
    <div class="line" style="top:354px; font-size:34px; line-height:36px;">Ethanol :</div>
    <div class="line" style="top:396px; font-size:60px; line-height:62px;">45%/55%</div>
    <div class="line" style="top:480px; font-size:19px; line-height:20px;">Produced by:</div>
    <div class="line bold" style="top:504px; font-size:28px; line-height:30px;">Harbor Stillhouse,</div>
    <div class="line" style="top:539px; font-size:16px; line-height:18px;">Lõunamaa 48213, Rannaküla, Sõstra 7</div>
    <div class="line bold" style="top:566px; font-size:23px; line-height:25px;">Made in Estonia.</div>
    <div class="line" style="top:601px; font-size:19px; line-height:24.3px;">Product is made of<br>Estonian apple wine and<br>distilled in reflux still<br>in small batches</div>
    <div class="line bold" style="top:706px; font-size:23px; line-height:25px;">Destillate 85%</div>
    <div class="line left-text" style="left:55px; top:759px; font-size:23px; line-height:25px;">Batch no:&nbsp; ..................</div>
    <div class="line" style="top:791px; font-size:19px; line-height:24px;">Produce with utmost pleasure<br>Consume responsibly</div>
    <div class="line left-text" style="left:60px; top:865px; font-size:22px; line-height:24px;">Distiller:</div>
  </section>

  <!-- Estonian back label -->
  <section class="label label-back-et" style="left:812px; top:32px; width:371px; height:947px;">
    <div class="label-halo"></div>
    <div class="label-frame" style="left:9px; top:22px; width:354px; height:904px;"></div>
    <div class="art-area" role="img" aria-label="Small red apple illustration with leaves and a white still-coil pattern" style="left:128px; top:35px; width:121px; height:151px;"></div>
    <div class="line wordmark" style="top:202px; font-size:26px; line-height:28px;">Orchardine</div>
    <div class="line product-title" style="top:247px; font-size:26px; line-height:28px;">Õunaveini destillaat</div>
    <div class="line" style="top:293px; font-size:28px; line-height:30px;">50 cl/35 cl</div>
    <div class="line" style="top:352px; font-size:34px; line-height:36px;">Ethanol :</div>
    <div class="line" style="top:395px; font-size:60px; line-height:62px;">45%/55%</div>
    <div class="line" style="top:483px; font-size:19px; line-height:20px;">Toodetud</div>
    <div class="line bold" style="top:507px; font-size:21px; line-height:23px;">Harbor Stillhouse OÜ poolt,</div>
    <div class="line" style="top:540px; font-size:16px; line-height:18px;">Lõunamaal 48213, Rannaküla, Sõstra 7</div>
    <div class="line" style="top:581px; font-size:21px; line-height:27px;">Toodetud Eestis,eestimaisest<br>õunaveinist ja destilleeritud<br>käsitööna väikeste<br>partiidena</div>
    <div class="line bold" style="top:694px; font-size:23px; line-height:25px;">Destillaat 85%</div>
    <div class="line left-text" style="left:49px; top:753px; font-size:23px; line-height:25px;">Partii nr:&nbsp; ..................</div>
    <div class="line" style="top:788px; font-size:19px; line-height:23px;">Toodetud puhtast roomust<br>Tarbige vastututstundlikult!</div>
    <div class="line left-text" style="left:60px; top:860px; font-size:22px; line-height:24px;">Meister:</div>
  </section>

</div>
</body>
</html>
```